Letterhead, stationery and email signature for construction business

I need the letterhead, stationery and email signature designs for a construction business. I want them to have a corporate feel to them.

I've attached the logo for reference.

```html
<!DOCTYPE html>
<html lang="en">
<head>
<meta charset="utf-8">
<title>Braxton Build Stationery</title>
<link rel="stylesheet" href="https://fonts.googleapis.com/css2?family=Arimo:wght@400;700&family=Montserrat:wght@500;600&display=swap">
<style>
  :root {
    --brand-blue: #2f55a0;
    --brand-slate: #4f4f5a;
    --body-text: #555559;
    --paper: #ffffff;
    --backdrop: #dedede;
    --footer-text: #ffffff;
  }
  * { margin: 0; padding: 0; box-sizing: border-box; }
  html, body { width: 891px; height: 1200px; overflow: hidden; }
  body { background: var(--backdrop); position: relative; font-family: "Arimo", Arial, sans-serif; color: var(--body-text); }

  .letterhead {
    position: absolute; left: 109px; top: 69px; width: 538px; height: 761px;
    background: var(--paper); box-shadow: 2px 3px 5px rgba(0,0,0,.25);
  }
  .brand { position: absolute; display: flex; align-items: center; gap: 7px; }
  .brand-mark { background: var(--brand-slate); flex: none; }
  .brand-name { font-family: "Arimo", Arial, sans-serif; font-weight: 700; color: var(--brand-blue); letter-spacing: .3px; white-space: nowrap; }
  .letterhead .brand { left: 48px; top: 113px; }
  .letterhead .brand-mark { width: 34px; height: 36px; }
  .letterhead .brand-name { font-size: 15px; }

  .greeting { position: absolute; left: 49px; top: 233px; font-family: "Montserrat", sans-serif; font-weight: 600; font-size: 12px; color: var(--body-text); }
  .letter-body { position: absolute; left: 48px; top: 268px; width: 442px; font-size: 8.6px; line-height: 11px; }
  .letter-body p { margin-bottom: 9.5px; }
  .closing { position: absolute; left: 49px; top: 498px; font-family: "Montserrat", sans-serif; font-weight: 600; font-size: 7px; color: var(--body-text); }
  .signature { position: absolute; left: 48px; top: 530px; width: 89px; height: 27px; background: linear-gradient(90deg, #d9d9dc, #eeeef0); border-radius: 3px; }

  .footer-band { position: absolute; background: var(--brand-blue); color: var(--footer-text); }
  .footer-mark { position: absolute; background: var(--brand-slate); }
  .footer-block { position: absolute; background: var(--brand-slate); }

  .letterhead .footer-band { left: 0; top: 703px; width: 424px; height: 41px; padding: 7px 0 0 48px; font-size: 9.6px; line-height: 14px; }
  .letterhead .footer-mark { left: 429px; top: 707px; width: 30px; height: 30px; }
  .letterhead .footer-block { left: 472px; top: 707px; width: 66px; height: 43px; }
  .contact-row { display: flex; align-items: center; gap: 4px; }
  .contact-row .item { display: inline-flex; align-items: center; gap: 4px; margin-right: 6px; }
  .icon { width: 8px; height: 8px; fill: none; stroke: currentColor; stroke-width: 1.1; flex: none; }

  .business-card {
    position: absolute; left: 105px; top: 908px; width: 546px; height: 182px;
    background: var(--paper); box-shadow: 2px 3px 5px rgba(0,0,0,.25);
  }
  .business-card .brand { left: 48px; top: 45px; gap: 9px; }
  .business-card .brand-mark { width: 40px; height: 48px; }
  .business-card .brand-name { font-size: 20px; }
  .card-divider { position: absolute; left: 297px; top: 30px; width: 1.5px; height: 92px; background: var(--brand-slate); }
  .card-person { position: absolute; left: 317px; top: 26px; }
  .person-name { font-weight: 700; font-size: 18px; color: var(--brand-blue); letter-spacing: .2px; line-height: 21px; }
  .person-role { font-size: 13px; color: var(--body-text); line-height: 15px; margin-bottom: 7px; }
  .card-contacts { list-style: none; font-size: 13px; line-height: 19px; color: var(--body-text); }
  .card-contacts li { display: flex; align-items: center; gap: 7px; }
  .card-contacts .icon { width: 10px; height: 10px; color: var(--brand-blue); }
  .business-card .footer-band { left: 0; top: 138px; width: 433px; height: 33px; text-align: center; font-size: 13px; line-height: 33px; }
  .business-card .footer-mark { left: 437px; top: 142px; width: 24px; height: 24px; }
  .business-card .footer-block { left: 471px; top: 141px; width: 75px; height: 34px; }
</style>
</head>
<body>

<section class="letterhead">
  <div class="brand">
    <span class="brand-mark"></span>
    <span class="brand-name">BRAXTON BUILD</span>
  </div>

  <p class="greeting">Dear Mr. Harlow,</p>

  <div class="letter-body">
    <p>Lorem ipsum dolor sit amet, consectetuer adipiscing elit, sed diam nonmmy nibh euismod tincidunt ut laor eet dolore magna aliquam erat volutpat. Ut wisi enim ad minim veniam, quis nostrud exerci tationmcorper suscipit lobortis nisl ut aliquip ex ea commodo consequat. Duis autem vel eum iriure dolor in hendrerit in vulputate velit esse molestie consequat, vel illum dolore eu feugiat</p>
    <p>Rorem ipsum dolor sit amet, consectetuer adipiscing elit, sed diam nonmmy nibh euismod tincidunt ut laor eet dolore magna aliquam erat volutpat. Ut wisi enim ad minim veniam, quis nostrud exerci tationmcorper suscipit lobortis nisl ut aliquip ex ea commodo consequat. Duis autem vel eum iriure dolor in hendrerit in vulputate velit esse molest</p>
    <p>Dorem ipsum dolor sit amet, consectetuer adipiscing elit, sed diam nonmmy nibh euismod tincidunt ut laor eet dolore magna aliquam erat volutpat. Ut wisi enim ad minim veniam, quis nostrud exerci tationmcorper suscipit lobortis nisl ut aliquip ex ea commodo consequat. Duis autem vel eum iriure dolor in hendrerit in suscipit lobortis nisl ut aliquip ex ea commodo consequat. Duis autem vel eum iriure dolor in hendrerit in vulputate velit esse molestie consequat, vel illum</p>
    <p>Sorem ipsum dolor sit amet, consectetuer adipiscing elit, sed diam nonmmy nibh euismod tincidunt ut laor eet dolore magna aliquam erat volutpat. Ut wisi enim ad minim veniam, quis nostrud exerci tationmcorper suscipit lobortis nisl ut aliquip ex ea commodo consequat. Duis autem vel eum iriure dolor in</p>
  </div>

  <p class="closing">Sincerely,</p>
  <div class="signature" role="img" aria-label="Handwritten signature of the sender"></div>

  <div class="footer-band">
    <div>Your Address, City, State, Zip 0000</div>
    <div class="contact-row">
      <span class="item">
        <svg class="icon" viewBox="0 0 10 10"><path d="M2 1.2 L3.6 1 L4.3 3 L3.2 3.8 Q4.2 5.9 6.2 6.8 L7 5.7 L9 6.4 L8.8 8 Q8.6 9 7.4 8.9 Q1.1 8.2 1.1 2.6 Q1.1 1.4 2 1.2 Z"/></svg>
        123-456-2100
      </span>
      <span class="item">
        <svg class="icon" viewBox="0 0 10 10"><rect x="1" y="2.2" width="8" height="5.6"/><path d="M1 2.4 L5 5.6 L9 2.4"/></svg>
        youremail@mailbox.com
      </span>
      <span class="item">
        <svg class="icon" viewBox="0 0 10 10"><circle cx="5" cy="5" r="4"/><ellipse cx="5" cy="5" rx="1.8" ry="4"/><path d="M1 5 H9 M1.6 3 H8.4 M1.6 7 H8.4"/></svg>
        www.yourwebsite.com
      </span>
    </div>
  </div>
  <div class="footer-mark"></div>
  <div class="footer-block"></div>
</section>

<section class="business-card">
  <div class="brand">
    <span class="brand-mark"></span>
    <span class="brand-name">BRAXTON BUILD</span>
  </div>

  <div class="card-divider"></div>

  <div class="card-person">
    <div class="person-name">DANIEL HARLOW</div>
    <div class="person-role">Manager</div>
    <ul class="card-contacts">
      <li>
        <svg class="icon" viewBox="0 0 10 10"><path d="M2 1.2 L3.6 1 L4.3 3 L3.2 3.8 Q4.2 5.9 6.2 6.8 L7 5.7 L9 6.4 L8.8 8 Q8.6 9 7.4 8.9 Q1.1 8.2 1.1 2.6 Q1.1 1.4 2 1.2 Z"/></svg>
        123-456-2100
      </li>
      <li>
        <svg class="icon" viewBox="0 0 10 10"><rect x="1" y="2.2" width="8" height="5.6"/><path d="M1 2.4 L5 5.6 L9 2.4"/></svg>
        youremail@mailbox.com
      </li>
      <li>
        <svg class="icon" viewBox="0 0 10 10"><circle cx="5" cy="5" r="4"/><ellipse cx="5" cy="5" rx="1.8" ry="4"/><path d="M1 5 H9 M1.6 3 H8.4 M1.6 7 H8.4"/></svg>
        www.yourwebsite.com
      </li>
    </ul>
  </div>

  <div class="footer-band">Your Address, City, State, Zip 0000</div>
  <div class="footer-mark"></div>
  <div class="footer-block"></div>
</section>

</body>
</html>
```